Real Estate Listing Signs for standard Yard arms

I need real estate listing signs done, for the standard sized sign to be hung beneath a white yard arm. To match existing logo. Information to be included:
-Logo
-Business name
-Phone number
-Marden Fosk Tundra Circle & Marden Fosk realty logos (smaller print)

Colors to be Red and anywhere in the gray scale between black and white, or a combination of those.

Target Market(s)

Drive by visuals

Industry/Entity Type

Real Estate Agent

Colors

Designer to choose only greyscale colors for use in the design.

Requirements
Must have
• My Logo and business name in same/similar font to whats provided, the MF tundra circle logo (small on bottom or corner somewhere), My phone number, and a decent amount of red coloration on the sign.

```html
<!DOCTYPE html>
<html lang="en">
<head>
<meta charset="utf-8">
<title>Corvane Realty – Yard Sign</title>
<link rel="stylesheet" href="https://fonts.googleapis.com/css2?family=Cinzel:wght@600;700;800&family=Oswald:wght@500&display=swap">
<style>
  :root {
    --red: #e21b23;
    --black: #1f1c1d;
    --ink: #111111;
    --white: #ffffff;
    --stage: #d9d9d9;
    --gray-deep: #d6d6d6;
    --gray-mid: #e6e6e6;
    --gray-light: #f3f3f3;
    --peach: #fbe6dc;
    --peach-soft: #fdf1eb;
  }
  html, body {
    margin: 0;
    width: 1200px;
    height: 1200px;
    overflow: hidden;
    background: var(--stage);
  }
  .sign {
    position: absolute;
    left: 30px;
    top: 173px;
    width: 1140px;
    height: 854px;
    background: var(--white);
    overflow: hidden;
    font-family: "Cinzel", serif;
  }
  .sign-texture {
    position: absolute;
    left: 0;
    top: 0;
    width: 720px;
    bottom: 120px;
    background:
      radial-gradient(ellipse 420px 520px at 120px 420px, var(--gray-deep) 0%, rgba(214,214,214,0) 100%),
      linear-gradient(100deg, var(--gray-mid) 0%, var(--gray-light) 45%, rgba(255,255,255,0) 100%);
  }
  .sign-watermark {
    position: absolute;
    left: 599px;
    top: 0;
    right: 0;
    bottom: 120px;
    background:
      radial-gradient(ellipse 260px 300px at 340px 560px, rgba(226,226,230,0.9) 0%, rgba(226,226,230,0) 100%),
      linear-gradient(160deg, rgba(253,241,235,0) 0%, var(--peach-soft) 30%, var(--peach) 100%);
  }
  .brand {
    position: absolute;
    left: 0;
    right: 0;
    top: 58px;
    text-align: center;
    z-index: 1;
  }
  .brand-square {
    display: block;
    width: 140px;
    height: 140px;
    margin: 0 auto;
    background: var(--red);
  }
  .brand-name {
    margin: 90px 0 0;
    font-size: 58px;
    font-weight: 700;
    color: var(--ink);
    letter-spacing: 3px;
    line-height: 1;
  }
  .agent-name {
    position: absolute;
    left: 0;
    right: 0;
    top: 442px;
    margin: 0;
    text-align: center;
    font-size: 92px;
    font-weight: 700;
    color: var(--red);
    letter-spacing: 5px;
    line-height: 1;
    white-space: nowrap;
    z-index: 1;
  }
  .contact {
    position: absolute;
    left: 0;
    right: 0;
    top: 540px;
    height: 56px;
    display: flex;
    justify-content: center;
    align-items: center;
    gap: 22px;
    font-size: 40px;
    font-weight: 700;
    color: var(--ink);
    white-space: nowrap;
    z-index: 1;
  }
  .contact-item { display: flex; align-items: center; gap: 16px; }
  .contact-divider { width: 2px; height: 56px; background: var(--ink); }
  .contact-icon { width: 40px; height: 40px; flex: none; }
  .footer {
    position: absolute;
    left: 0;
    right: 0;
    bottom: 0;
    height: 120px;
    display: flex;
    z-index: 1;
  }
  .footer-brokerage {
    width: 570px;
    background: var(--black);
    display: flex;
    align-items: center;
    justify-content: center;
    font-family: "Oswald", sans-serif;
    font-weight: 500;
    font-size: 36px;
    color: var(--white);
    letter-spacing: 1px;
  }
  .footer-disclaimer {
    flex: 1;
    background: var(--red);
    display: flex;
    align-items: center;
    justify-content: center;
    text-align: center;
    font-size: 26px;
    font-weight: 700;
    line-height: 1.2;
    color: var(--white);
    letter-spacing: 1px;
  }
</style>
</head>
<body>
  <main class="sign">
    <div class="sign-texture" role="img" aria-label="Soft grey geometric pattern of diamonds and dots"></div>
    <div class="sign-watermark" role="img" aria-label="Large faint decorative backdrop in pale peach and grey"></div>

    <header class="brand">
      <span class="brand-square"></span>
      <p class="brand-name">CORVANE REALTY</p>
    </header>

    <h1 class="agent-name">JORDAN CORVANE</h1>

    <div class="contact">
      <span class="contact-item">
        <svg class="contact-icon" viewBox="0 0 24 24" aria-hidden="true">
          <path fill="#e21b23" d="M6.6 2.5 9.3 6.3 7.6 8.5c1.2 2.7 3.2 4.8 5.9 6l2.2-1.7 3.8 2.7-1.3 3.3c-.4 1-1.5 1.6-2.6 1.3C8.8 18.4 4.1 13.7 2.4 7c-.3-1.1.3-2.2 1.3-2.6z"/>
          <path fill="none" stroke="#e21b23" stroke-width="1.6" stroke-linecap="round" d="M14 5.5a5 5 0 0 1 4.5 4.5M14.5 2a8.5 8.5 0 0 1 7.5 7.5"/>
        </svg>
        907-555-0148
      </span>
      <span class="contact-divider"></span>
      <span class="contact-item">
        <svg class="contact-icon" viewBox="0 0 24 24" aria-hidden="true">
          <rect x="1" y="4" width="22" height="16" fill="#e21b23"/>
          <path fill="none" stroke="#ffffff" stroke-width="1.5" d="M1 4l11 9 11-9M1 20l8-8M23 20l-8-8"/>
        </svg>
        JCORVANE@MAILBOX.TEST
      </span>
    </div>

    <footer class="footer">
      <div class="footer-brokerage">MARDEN FOSK TUNDRA CIRCLE</div>
      <div class="footer-disclaimer">EACH OFFICE INDEPENDENTLY<br>OWNED AND OPERATED</div>
    </footer>
  </main>
</body>
</html>
```